Brochure Design Project for Building Designer

I need a modern and edgy brochure to introduce my new business TORV Design, Commercial and Residential Building Designers.

We specialise in Building Design, Project Management and Design Consultation.

I would like the brochure to be anywhere between 2-4 pages, depending of amount of suitable content available.
Colours to be black and white with splashes of
bright colours (mostly incorporated in photos).

Main Content of brochure to be broken up into 3 (maybe 4) sections to include:

About Us
Services
Projects

Logo Text (DESIGN etc) can be changed to white if suits better with black background.

Would be nice to include sketches to give it that architectural feel.

Samples and wording will be uploaded shortly
Updates

I HAVE PROVIDED A COMPLETE UPDATE OF PROJECT REQUIREMENTS INCLUDING ALL NEW UPLOADED FILES.

PLEASE REFER TO THE BROCHURE LAYOUT PDF UPLOADEDĀ FOR FULL INFORMATION ON PROJECT INCLUDING BROCHURE LAYOUT.

IF YOU HAVE ANY QUESTIONS OR REQUIRE ANY FURTHER INFORMATION, PLEASE LET ME KNOW

I HAVE ADDED FURTHER DEVELOPED PDF DOCUMENTS OF BROCHURE.

IF YOU HAVE TROUBLE OPENING THESE DOCS IN ADOBE ILLUSTRATOR THRU ADOBE BRIDGE PLEASE LET ME KNOW & I WILL UPLOAD AI FILES.

CAN YOU PLEASE FINE TUNE GRAPHICS AND WORK ON BACKGROUND

Target Market(s)

Builders, Property Developers, Architects, Consultants, Professionals

Industry/Entity Type

Business

Requirements
Must have
• Very Professional Look
Black and White
Simple and easy to read layout
Either A4 (if only 2 pages) or
A3 double sided with centre fold (if 4 pages)
Touch up of photos (if possible) to make them stand out of the page.
Samples of recent projects with photos
Should not have
• Any comics or similar

```html
<!DOCTYPE html>
<html lang="en">
<head>
<meta charset="utf-8">
<title>TORV Design – About Us &amp; Services</title>
<link rel="stylesheet" href="https://fonts.googleapis.com/css2?family=Fira+Sans:wght@400;500;700&family=Fira+Sans+Condensed:wght@700&display=swap">
<style>
  :root {
    --backdrop: #e4e4e6;
    --ink: #111111;
    --black: #000000;
    --paper: #f8f8f4;
    --accent: #e5197e;
    --ghost: #c9c9c9;
    --photo-warm: #c9a977;
    --photo-light: #efe3c6;
    --photo-dark: #3a2a1e;
  }
  * { margin: 0; padding: 0; box-sizing: border-box; }
  html, body {
    width: 1200px; height: 872px; overflow: hidden;
    background: var(--backdrop);
  }
  .spread {
    position: absolute; left: 75px; top: 73px;
    width: 1042px; height: 733px;
    background: var(--black);
    overflow: hidden;
    font-family: "Fira Sans", Arial, sans-serif;
    color: var(--ink);
  }
  .spread__shapes { position: absolute; inset: 0; }
  .feature-photo {
    position: absolute; left: 0; top: 122px; width: 326px; height: 505px;
    background:
      linear-gradient(90deg, rgba(248,248,244,0) 45%, var(--paper) 100%),
      linear-gradient(180deg, var(--photo-light) 0%, var(--photo-warm) 45%, var(--photo-dark) 75%, var(--photo-light) 100%);
  }
  .section-title {
    position: absolute;
    font-family: "Fira Sans Condensed", "Arial Narrow", sans-serif;
    font-weight: 700; font-size: 41px; letter-spacing: 0.5px;
    line-height: 1; white-space: nowrap;
    transform-origin: left top; transform: rotate(-90deg);
  }
  .section-title--ghost {
    color: transparent;
    -webkit-text-stroke: 1px var(--ghost);
    font-size: 44px;
  }
  .about-title { left: 380px; top: 290px; }
  .about-title.section-title--ghost { left: 402px; top: 310px; }
  .services-title { left: 380px; top: 570px; }
  .services-title.section-title--ghost { left: 402px; top: 593px; }

  .copy {
    position: absolute; font-size: 12.4px; line-height: 14.6px;
    text-transform: uppercase; letter-spacing: 0.2px;
  }
  .bullets { list-style: none; position: absolute; font-size: 12.4px; line-height: 16.8px; text-transform: uppercase; letter-spacing: 0.2px; }
  .bullets li { position: relative; padding-left: 11px; white-space: nowrap; }
  .bullets li::before {
    content: ""; position: absolute; left: 0; top: 6px;
    width: 5px; height: 5px; border-radius: 50%; background: var(--accent);
  }
  .intro { left: 465px; top: 96px; width: 540px; }
  .experience--a { left: 465px; top: 133px; }
  .experience--b { left: 814px; top: 133px; }
  .quote {
    position: absolute; left: 465px; top: 232px; width: 560px;
    font-weight: 700; font-size: 34px; line-height: 38px;
    color: var(--accent); text-transform: uppercase; letter-spacing: 1px;
  }
  .quote__line2 { padding-left: 18px; }
  .quote__author { position: absolute; left: 482px; top: 312px; font-size: 11px; font-weight: 500; }
  .ethos { left: 465px; top: 341px; width: 540px; }
  .services-intro { left: 470px; top: 398px; }
  .services-list { left: 470px; top: 424px; }
  .drafting { left: 470px; top: 606px; width: 520px; }
</style>
</head>
<body>
<main class="spread">
  <div class="feature-photo" role="img" aria-label="Warm-lit open-plan interior with a dining table, chairs and a steel staircase"></div>
  <svg class="spread__shapes" width="1042" height="733" viewBox="0 0 1042 733" aria-hidden="true">
    <polygon points="435,52 1042,27 1042,700 525,703 326,585 326,122" fill="#f8f8f4"/>
    <line x1="415" y1="7" x2="1042" y2="27" stroke="#9a9a9a" stroke-width="0.8"/>
    <line x1="326" y1="122" x2="415" y2="7" stroke="#6a6a6a" stroke-width="0.8"/>
  </svg>

  <h2 class="section-title section-title--ghost about-title" aria-hidden="true">ABOUT US</h2>
  <h2 class="section-title about-title">ABOUT US</h2>
  <h2 class="section-title section-title--ghost services-title" aria-hidden="true">SERVICES</h2>
  <h2 class="section-title services-title">SERVICES</h2>

  <p class="copy intro">TORV Design has a diverse portfolio of commercial + residential work across a range of scales, budgets + project types. Areas of experience include:</p>
  <ul class="bullets experience--a">
    <li>Commercial developments</li>
    <li>Mixed-use developments</li>
    <li>Residential &amp; multi residential</li>
    <li>Upmarket individual houses</li>
    <li>Residential + commercial interior fitouts</li>
  </ul>
  <ul class="bullets experience--b">
    <li>Healthcare</li>
    <li>Commercial industrial</li>
    <li>Cafes/restaurants</li>
    <li>Alterations + additions</li>
  </ul>

  <blockquote class="quote">
    <div>“Simplicity is the ultimate</div>
    <div class="quote__line2">sophistication”</div>
  </blockquote>
  <p class="quote__author">- Aldo Verani</p>

  <p class="copy ethos">We strive to be efficient at all times in every aspect of our service + pride ourselves on our attention to detail.</p>

  <p class="copy services-intro">We are able to provide a wide range of services:</p>
  <ul class="bullets services-list">
    <li>Project planning</li>
    <li>Design concepts</li>
    <li>Design development / development approval</li>
    <li>Consultant liaison + management</li>
    <li>Building certification</li>
    <li>Tender / construction documentation</li>
    <li>Project management</li>
    <li>3D modelling &amp; renders</li>
    <li>Re-documentation &amp; design consultation</li>
    <li>Drafting services</li>
  </ul>
  <p class="copy drafting">We offer high quality drafting solutions for pre-designed projects of any size to ensure you get the best quality drawings for local authority + construction issue.</p>
</main>
</body>
</html>
```